Harborline Crest Insurance Services

we are a high end insurance agency we specialize on Auto | Home | Business | Life looking for something professional and luxuries at the same time. if you guys need anything else please let me know.

Auto | Home | Business | Life must be under logo on the back with black background.

i want the back part to be black with our gold logo on it.

Target Market(s)

Auto | Home | Business | Life

Industry/Entity Type

Insurance Broker

Contact Information for Business Card

My logo is gold so a black in the back would be nice.

Font styles to use
Serif

Colors
000000

Requirements
Must have
• Big logo on the back with black background.

```html
<!DOCTYPE html>
<html lang="en">
<head>
<meta charset="utf-8">
<title>Harborline Crest Insurance Services – Business Card</title>
<link href="https://fonts.googleapis.com/css2?family=Cinzel:wght@600&family=Open+Sans:wght@400;700&display=swap" rel="stylesheet">
<style>
  :root {
    --backdrop: #2b2b2b;
    --card: #000000;
    --gold: #e8b424;
    --gold-text: #d9a92a;
    --white: #f2f2f2;
  }
  * { margin: 0; padding: 0; box-sizing: border-box; }
  html, body { width: 1200px; height: 900px; overflow: hidden; }
  body { background: var(--backdrop); position: relative; font-family: "Open Sans", Arial, sans-serif; }

  .card {
    position: absolute;
    top: 302px;
    width: 513px;
    height: 295px;
    background: var(--card);
    border-radius: 28px;
    box-shadow: 0 6px 14px rgba(0,0,0,0.55);
  }
  .card--front { left: 73px; }
  .card--back { left: 616px; }

  .wordmark {
    font-family: "Cinzel", "Times New Roman", serif;
    font-weight: 600;
    color: var(--gold);
    text-align: center;
    line-height: 1;
  }
  .wordmark__name { display: block; }
  .wordmark__sub { display: block; letter-spacing: 0.22em; }

  .card--front .wordmark {
    position: absolute;
    left: 0; right: 0; top: 104px;
    display: flex; align-items: center; justify-content: center; gap: 16px;
  }
  .card--front .wordmark__mark {
    width: 18px; height: 18px; border-radius: 50%; background: var(--gold);
  }
  .card--front .wordmark__name { font-size: 34px; }
  .card--front .wordmark__sub { font-size: 12.5px; margin-top: 8px; }

  .services {
    position: absolute;
    left: 0; right: 0; top: 252px;
    text-align: center;
    font-family: "Cinzel", "Times New Roman", serif;
    font-weight: 600;
    font-size: 15px;
    letter-spacing: 0.2em;
    color: var(--gold-text);
  }
  .services .sep { margin: 0 2px 0 0; letter-spacing: 0; }

  .card--back .wordmark {
    position: absolute;
    left: 22px; width: 210px; top: 120px;
  }
  .card--back .wordmark__name { font-size: 19px; }
  .card--back .wordmark__sub { font-size: 8.5px; margin-top: 6px; }

  .divider {
    position: absolute;
    left: 242px; top: 46px;
    width: 1px; height: 206px;
    background: var(--gold-text);
  }

  .contact {
    position: absolute;
    left: 263px; top: 50px;
    color: var(--white);
    font-size: 13.5px;
    line-height: 19.5px;
  }
  .contact__name { color: var(--gold-text); font-weight: 700; font-size: 13.5px; }
  .contact__lines { margin-top: 11px; list-style: none; }
  .contact__lines li { display: flex; align-items: center; gap: 5px; }
  .contact__lines svg { width: 11px; height: 11px; fill: var(--gold-text); flex: none; }
  .contact__address { margin-top: 11px; font-style: normal; }
  .contact__web { color: var(--gold-text); }
</style>
</head>
<body>
  <section class="card card--front">
    <div class="wordmark">
      <span class="wordmark__mark"></span>
      <div>
        <span class="wordmark__name">Harborline Crest</span>
        <span class="wordmark__sub">Insurance Services</span>
      </div>
    </div>
    <p class="services">Auto <span class="sep">|</span> Home <span class="sep">|</span> Business <span class="sep">|</span> Life</p>
  </section>

  <section class="card card--back">
    <div class="wordmark">
      <span class="wordmark__name">Harborline Crest</span>
      <span class="wordmark__sub">Insurance Services</span>
    </div>
    <div class="divider"></div>
    <div class="contact">
      <p class="contact__name">MARCO DELGADO</p>
      <p>License # 0K58104</p>
      <ul class="contact__lines">
        <li><svg viewBox="0 0 12 12"><path d="M2.5 1l2 2.2-1 1.3c.7 1.5 2 2.8 3.5 3.5l1.3-1 2.2 2-1.2 1.8C5.5 10.5 1.5 6.5 1 2.2z"/></svg>555-318-2046</li>
        <li><svg viewBox="0 0 12 12"><path d="M3.5 0.5h5v11h-5zM4.5 1.5v8h3v-8z"/></svg>555-724-9130</li>
        <li><svg viewBox="0 0 12 12"><path d="M3 1h6v3H3zM1 4.5h10v5H9v-2H3v2H1zM3.5 8h5v3h-5z"/></svg>555-461-7783</li>
        <li><svg viewBox="0 0 12 12"><path d="M1 2.5h10v1L6 7 1 3.5zM1 4.7l5 3.5 5-3.5V10H1z"/></svg>mdelgado@harborlinecrest.com</li>
      </ul>
      <address class="contact__address">
        2450 Seaview Avenue<br>
        Port Alder, CA 90000<br>
        <span class="contact__web">www.harborlinecrest.com</span>
      </address>
    </div>
  </section>
</body>
</html>
```